Social Media Templates for Ambervale Kinship

We need a set of Square (1080 x 1080) social media posts.

My company works with sports clubs, helping them to raise money with a lottery.

I need a set of social media image that I can use to appeal to new Ambervale Kinship to encourage them to start a lottery with us.

This landing page has worked very well for us https://ambervalekinship.com/ambervale-kinship/

THING THAT APPEAL TO CLUBS

No Setup Fees/Start for Free - (We don’t charge any registration fees, or setup fees so you can start raising money from the first draw.)

Start Straight Away - (A club can start raising money straight away.)

Sustainable Income - (The average player plays for 7 years)

Subscription Lottery - (once a player joins, they play until the choose to leave. A club doesn't have to sell tickets every draw to the same people)

All Administration Taken Care Of - (We do all the hard work, so they can focus on running their club.)

Unlimited Income - (There is no limit on the amount of money a club can raise: the more players, the more funds for the club.)

Fundraising reach - (Reach new fans)

50% of the sales is guaranteed profit

£25,000 jackpot - (a person could win £25,000 every week)

Price - (It costs just £1 per week to enter)

Help Your Club - (100% of the profit goes to the club who a player chooses to support)

You can see all the clubs we work with on www.ambervalekinship.com

The images will also be used on Facebook. You can see some examples here https://www.friendvista.com/AmbervaleKinship/ (you may need a proxy to view this page as it is only viewable in the UK, so I have attached some screenshots)

You can find the Ambervale Kinship Logo here https://www.logocrate.com/quillmarshco/

Target Market(s)

People who are involved with amateur sports in United Kingdom

Industry/Entity Type

Gambling

Font styles to use
Sans Serif

Requirements
Must have
• My project must look great on social social media and encourage people to get in touch about starting a lottery with us.

Adobe Suite files must be provided

```html
<!DOCTYPE html>
<html lang="en">
<head>
<meta charset="utf-8">
<title>Ambervale Kinship – Start for Free Social Post</title>
<link rel="stylesheet" href="https://fonts.googleapis.com/css2?family=Barlow+Semi+Condensed:wght@800&display=swap">
<style>
  :root {
    --page: #ffffff;
    --navy: #0d1f3f;
    --navy-deep: #081631;
    --sky: #e6e0c8;
    --stand: #8a9cb4;
    --kit-light: #3456a6;
    --kit: #1f3d8c;
    --kit-dark: #15295e;
    --brand-blue: #1d7ac4;
    --white: #ffffff;
    --yellow: #fff200;
  }
  * { margin: 0; padding: 0; box-sizing: border-box; }
  html, body {
    width: 1200px;
    height: 1000px;
    overflow: hidden;
    background: var(--page);
  }
  .post {
    position: absolute;
    left: 170px;
    top: 70px;
    width: 860px;
    height: 860px;
    background: var(--navy);
    overflow: hidden;
    font-family: "Barlow Semi Condensed", "Arial Narrow", sans-serif;
    font-weight: 800;
    text-transform: uppercase;
    line-height: 1;
  }
  .post-art {
    position: absolute;
    inset: 0;
  }
  .brand {
    position: absolute;
    left: 60px;
    top: 78px;
    display: flex;
    align-items: center;
    gap: 14px;
  }
  .brand-mark {
    width: 22px;
    height: 22px;
    background: var(--brand-blue);
  }
  .brand-name {
    color: var(--white);
    font-size: 40px;
    line-height: 1.02;
  }
  .offer {
    position: absolute;
    left: 72px;
    top: 573px;
  }
  .offer-lead {
    color: var(--white);
    font-size: 50px;
    margin-bottom: 9px;
  }
  .offer-jackpot {
    color: var(--white);
    font-size: 88px;
    margin-bottom: 8px;
  }
  .offer-price {
    color: var(--yellow);
    font-size: 59px;
  }
</style>
</head>
<body>
  <main class="post">
    <svg class="post-art" width="860" height="860" viewBox="0 0 860 860">
      <defs>
        <linearGradient id="photoTone" x1="0" y1="0" x2="0" y2="1">
          <stop offset="0" stop-color="var(--sky)"/>
          <stop offset="0.22" stop-color="var(--sky)"/>
          <stop offset="0.3" stop-color="var(--stand)"/>
          <stop offset="0.45" stop-color="var(--kit-light)"/>
          <stop offset="0.75" stop-color="var(--kit)"/>
          <stop offset="1" stop-color="var(--kit-dark)"/>
        </linearGradient>
        <linearGradient id="photoSide" x1="0" y1="0" x2="1" y2="0">
          <stop offset="0" stop-color="var(--navy)" stop-opacity="0.55"/>
          <stop offset="0.35" stop-color="var(--navy)" stop-opacity="0"/>
          <stop offset="1" stop-color="var(--navy)" stop-opacity="0.15"/>
        </linearGradient>
        <linearGradient id="textShade" x1="0" y1="0" x2="0.8" y2="0.6">
          <stop offset="0" stop-color="var(--navy-deep)" stop-opacity="0.75"/>
          <stop offset="0.6" stop-color="var(--navy-deep)" stop-opacity="0.35"/>
          <stop offset="1" stop-color="var(--navy-deep)" stop-opacity="0"/>
        </linearGradient>
        <linearGradient id="panelGlow" x1="0" y1="0" x2="0" y2="1">
          <stop offset="0" stop-color="var(--white)" stop-opacity="0.35"/>
          <stop offset="1" stop-color="var(--white)" stop-opacity="0"/>
        </linearGradient>
      </defs>
      <polygon class="team-photo" role="img"
        aria-label="Photo: a youth football team in blue shirts huddling with their smiling coach on a sunny pitch"
        points="300,8 860,0 860,860 240,860 172,528" fill="url(#photoTone)"/>
      <polygon class="photo-shade" points="300,8 860,0 860,860 240,860 172,528" fill="url(#photoSide)"/>
      <polygon class="light-panel" points="470,0 740,0 715,95 715,330 470,60" fill="url(#panelGlow)"/>
      <polygon class="text-shade" points="0,470 560,560 700,860 0,860" fill="url(#textShade)"/>
      <line class="dotted-rule" x1="193" y1="238" x2="115" y2="530"
        stroke="var(--white)" stroke-width="2" stroke-dasharray="2 4"/>
      <polyline class="frame-line" points="715,0 715,95 822,188 710,592 860,632"
        fill="none" stroke="var(--white)" stroke-width="3"/>
      <line class="frame-line" x1="860" y1="640" x2="765" y2="860"
        stroke="var(--white)" stroke-width="3"/>
    </svg>

    <div class="brand">
      <span class="brand-mark"></span>
      <span class="brand-name">Ambervale<br>Kinship</span>
    </div>

    <section class="offer">
      <p class="offer-lead">Start for free</p>
      <p class="offer-jackpot">£25,000 Jackpot</p>
      <p class="offer-price">£1 per week to enter</p>
    </section>
  </main>
</body>
</html>
```